Natural Skin Care e commerce website

we are the distributor for natural skincare product , we would like to develop a e commerce website which encompass the ability to divide the product into face, body , baby , and base on ingredient , best seller, we are Olvexa certified product the key point to focus is natural organic , no nasties, vegan , unpolluted , full of natural ingredient. manuka, olive nordic style temporary style website is preferred. the website name is Quillom store.co , the web must have ability to take the order and let the brand upload their products

```html
<!DOCTYPE html>
<html lang="en">
<head>
<meta charset="utf-8">
<title>Quillom Store — Natural Skincare</title>
<link href="https://fonts.googleapis.com/css2?family=Roboto:wght@400;500;700&family=Mulish:wght@400;600;700&display=swap" rel="stylesheet">
<style>
:root{
  --pink:#f9b3cc;
  --pink-strong:#ee6f9c;
  --blush:#fcf4f5;
  --ink:#111111;
  --text:#555555;
  --muted:#8a8a8a;
  --star:#f7941d;
  --footer:#151515;
  --white:#ffffff;
}
*{margin:0;padding:0;box-sizing:border-box}
html,body{width:1200px;height:3884px;overflow:hidden;background:var(--white)}
body{position:relative;font-family:'Mulish',sans-serif;color:var(--ink)}
.abs{position:absolute}
.heading{font-family:'Roboto',sans-serif;font-weight:500;font-size:40px;letter-spacing:.5px;text-align:center;left:0;width:1200px;line-height:48px}

/* hero */
.hero{left:0;top:0;width:1200px;height:581px;
  background:
    radial-gradient(ellipse 230px 120px at 110px 40px,#d9d7d2 0%,rgba(217,215,210,.55) 55%,transparent 100%),
    radial-gradient(ellipse 70px 240px at 600px 250px,#3a2a1f 0%,rgba(58,42,31,.7) 60%,transparent 100%),
    radial-gradient(ellipse 90px 70px at 780px 430px,#2a2624 0%,rgba(42,38,36,.6) 60%,transparent 100%),
    radial-gradient(ellipse 60px 50px at 870px 395px,#c9c6c2 0%,transparent 100%),
    radial-gradient(ellipse 90px 45px at 970px 530px,#e4e2de 0%,transparent 100%),
    radial-gradient(ellipse 130px 160px at 1170px 500px,#4f6a2e 0%,rgba(79,106,46,.5) 55%,transparent 100%),
    linear-gradient(150deg,transparent 30%,#9a7048 46%,#b48456 58%,#8d6540 70%,transparent 84%),
    linear-gradient(120deg,#a8a49e 0%,#8b8780 40%,#7b766f 70%,#9c9892 100%)}
.hero-shade{inset:0;background:rgba(20,15,10,.32)}
.nav{top:44px;left:89px;display:flex;gap:20px;font-family:'Roboto',sans-serif;font-weight:700;font-size:14px;color:var(--white)}
.nav .active{color:var(--pink)}
.brand{top:28px;left:540px;display:flex;align-items:center;gap:12px;color:var(--white);font-family:'Roboto',sans-serif;font-weight:500;font-size:33px}
.brand .dot{width:28px;height:28px;border:3px solid var(--white);border-radius:50%}
.tools{top:38px;left:952px;display:flex;gap:16px}
.hero-title{top:180px;left:0;width:1200px;text-align:center;font-family:'Roboto',sans-serif;font-weight:700;font-size:54px;line-height:64px;color:var(--white)}
.hero-text{top:254px;left:250px;width:700px;text-align:center;font-family:'Roboto',sans-serif;font-size:19px;line-height:33px;color:var(--white)}
.btn-fill{background:var(--pink);color:var(--ink);font-family:'Roboto',sans-serif;font-weight:700;display:flex;align-items:center;justify-content:center}

/* categories */
.tile{top:766px;width:328px;height:362px;display:flex;align-items:center;justify-content:center;font-family:'Roboto',sans-serif;font-weight:500;font-size:32px}
.tile-face{background:
  radial-gradient(circle at 70px 70px,#fbe2e6 0%,#f7d3da 45%,transparent 62%),
  radial-gradient(circle at 270px 90px,#f2b893 0%,#eaa884 40%,transparent 62%),
  radial-gradient(circle at 50px 330px,#fbe0e4 0%,transparent 55%),
  radial-gradient(ellipse 60px 90px at 230px 320px,#f8e1d7 0%,transparent 100%),
  #f4c3cf}
.tile-body{background:
  radial-gradient(circle at 300px 120px,#f4c9c4 0%,#e9b3ae 30%,transparent 55%),
  radial-gradient(ellipse 30px 70px at 170px 120px,#f3eaa6 0%,transparent 100%),
  radial-gradient(circle at 60px 320px,#9c8a6a 0%,transparent 30%),
  radial-gradient(circle at 300px 340px,#a69a6e 0%,transparent 30%),
  radial-gradient(circle at 50px 30px,#cbb57a 0%,transparent 25%),
  #f7c7d7}
.tile-baby{background:
  radial-gradient(circle at 160px 260px,#f3b4b8 0%,#f1c3c9 35%,transparent 55%),
  radial-gradient(ellipse 90px 120px at 280px 120px,#f9dde5 0%,transparent 100%),
  radial-gradient(ellipse 60px 100px at 60px 120px,#f8dbe3 0%,transparent 100%),
  radial-gradient(ellipse 80px 50px at 50px 340px,#fbe5ec 0%,transparent 100%),
  #f4c6d3}

/* products */
.band{left:0;top:1229px;width:1200px;height:736px;background:var(--blush)}
.card{top:1353px;width:326px;height:530px;background:var(--white);box-shadow:0 0 6px rgba(0,0,0,.12);overflow:hidden}
.card .shot{position:absolute;left:12px;top:12px;width:302px;height:256px}
.card h3{position:absolute;left:9px;top:296px;font-family:'Roboto',sans-serif;font-weight:500;font-size:21px;line-height:26px;white-space:nowrap}
.card .price{position:absolute;left:9px;top:334px;font-family:'Roboto',sans-serif;font-size:21px;line-height:26px}
.card .stars{position:absolute;left:9px;top:371px;display:flex;gap:6px}
.card p{position:absolute;left:9px;top:402px;width:300px;font-size:16px;line-height:24px;color:var(--text)}
.card .cart{position:absolute;left:9px;top:469px;width:133px;height:37px;border:2px solid var(--pink);font-family:'Roboto',sans-serif;font-weight:700;font-size:13px;display:flex;align-items:center;justify-content:center;background:var(--white)}
.card .cart.on{background:var(--pink)}
.ribbon{left:-28px;top:14px;width:120px;height:26px;background:#e3141b;transform:rotate(-45deg);transform-origin:center;color:#fff;font-family:'Mulish',sans-serif;font-weight:700;font-size:9px;line-height:11px;text-align:center;padding-top:2px}
.dots{display:flex;gap:10px}
.dots i{width:11px;height:11px;border-radius:50%;background:var(--ink)}
.dots i.on{background:var(--pink)}

/* reviews */
.quote{width:308px;height:178px;background:var(--white);border-radius:8px;box-shadow:0 2px 10px rgba(0,0,0,.15);padding:18px 18px;font-size:14px;line-height:25px;color:var(--muted);text-align:justify}
.quote::after{content:"";position:absolute;left:144px;bottom:-10px;border:10px solid transparent;border-bottom:0;border-top-color:var(--white)}
.name{font-family:'Roboto',sans-serif;font-weight:500;font-size:19px;text-align:center;width:308px}

/* promo */
.promo{left:0;top:2610px;width:1200px;height:573px;background:
  radial-gradient(ellipse 230px 240px at 70px 130px,#3f6b2a 0%,rgba(63,107,42,.55) 50%,transparent 100%),
  radial-gradient(ellipse 140px 120px at 40px 470px,#e4d6b0 0%,rgba(228,214,176,.5) 60%,transparent 100%),
  radial-gradient(circle at 290px 390px,#ffffff 0%,#f1f1ef 35%,transparent 60%),
  radial-gradient(circle at 250px 490px,#cfe9d5 0%,#bfe0c8 30%,transparent 55%),
  radial-gradient(circle at 420px 455px,#b88a5a 0%,rgba(184,138,90,.5) 45%,transparent 65%),
  radial-gradient(ellipse 110px 100px at 970px 450px,#e7d2ac 0%,#dcc39a 45%,transparent 80%),
  radial-gradient(ellipse 160px 160px at 1100px 130px,#ffffff 0%,#f4f4f2 60%,transparent 100%),
  radial-gradient(ellipse 90px 70px at 1170px 330px,#f0f0ec 0%,transparent 100%),
  radial-gradient(ellipse 40px 20px at 1020px 310px,#3e5f25 0%,transparent 100%),
  radial-gradient(ellipse 70px 100px at 780px 520px,#4f7a3b 0%,transparent 100%),
  linear-gradient(135deg,#e6e7e3 0%,#f2f2f0 45%,#e7e6e1 100%)}
.promo-veil{left:300px;top:2660px;width:600px;height:400px;background:radial-gradient(ellipse at center,rgba(246,246,244,.9) 0%,rgba(246,246,244,.6) 55%,transparent 80%)}
.new{left:557px;top:2694px;width:92px;height:92px;border-radius:50%;background:var(--pink);display:flex;align-items:center;justify-content:center;font-family:'Roboto',sans-serif;font-weight:500;font-size:28px}
.promo-title{top:2806px;left:0;width:1200px;text-align:center;font-family:'Roboto',sans-serif;font-weight:500;font-size:34px;line-height:40px}
.promo-sub{top:2848px;left:0;width:1200px;text-align:center;font-family:'Roboto',sans-serif;font-weight:500;font-size:27px;line-height:32px;color:var(--pink-strong)}
.promo-rule{top:2897px;left:340px;width:534px;height:1px;background:#999}
.promo-text{top:2906px;left:340px;width:534px;text-align:center;font-family:'Roboto',sans-serif;font-size:16px;line-height:26px;color:#333}

/* newsletter */
.field{left:185px;top:3366px;width:551px;height:71px;border:2px solid #444;display:flex;align-items:center;padding-left:22px;gap:20px;font-size:19px;color:#555}

/* footer */
.footer{left:0;top:3521px;width:1200px;height:363px;background:var(--footer);color:var(--white)}
.f-head{font-family:'Roboto',sans-serif;font-weight:500;font-size:21px;top:3574px;color:var(--white)}
.f-list{top:3622px;font-size:16px;line-height:32px;list-style:none;color:var(--white)}
.pay{top:3834px;left:822px;display:flex;gap:9px}
.pay span{width:40px;height:24px;border-radius:3px;background:#e9e9e9}
</style>
</head>
<body>

<!-- hero -->
<section class="abs hero" role="img" aria-label="Amber skincare bottles and jars on a wooden board with white towels, a brush and green leaves">
  <div class="abs hero-shade"></div>
</section>
<nav class="abs nav"><span class="active">HOME</span><span>PRODUCTS</span><span>BLOG</span><span>REVIEW</span><span>CONTACT US</span></nav>
<div class="abs brand"><span class="dot"></span>QUILLOM</div>
<div class="abs tools">
  <svg width="22" height="22" viewBox="0 0 22 22" fill="none" stroke="#fff" stroke-width="3"><circle cx="9" cy="9" r="6.5"/><path d="M14 14l6 6"/></svg>
  <svg width="22" height="22" viewBox="0 0 22 22" fill="none" stroke="#fff" stroke-width="2"><circle cx="11" cy="11" r="9"/><path d="M2 11h18M11 2c4 4 4 14 0 18M11 2c-4 4-4 14 0 18"/></svg>
  <svg width="20" height="22" viewBox="0 0 20 22" fill="#fff"><circle cx="10" cy="6" r="5"/><path d="M1 21c0-6 4-9 9-9s9 3 9 9z"/></svg>
  <svg width="28" height="24" viewBox="0 0 28 24" fill="#fff"><path d="M0 3h5l3 12h13l3-9H8" stroke="#fff" stroke-width="2.5" fill="none"/><circle cx="10" cy="20" r="2.2"/><circle cx="19" cy="20" r="2.2"/><circle cx="23" cy="4" r="4" fill="#ee6f9c"/></svg>
</div>
<h1 class="abs hero-title">QUILLOM</h1>
<p class="abs hero-text">Lorem ipsum dolor sit amet, consectetur adipiscing elit, sed do eiusmod tempor incididunt ut labore et dolore magna aliqua.</p>
<div class="abs btn-fill" style="left:495px;top:341px;width:211px;height:62px;font-size:23px">SHOP NOW</div>

<!-- categories -->
<h2 class="abs heading" style="top:675px">CATEGORIES</h2>
<div class="abs tile tile-face" style="left:89px" role="img" aria-label="Pink face cream bowls, a loofah sponge and a cosmetic bottle on pink background">FACE</div>
<div class="abs tile tile-body" style="left:436px" role="img" aria-label="Body cream tube and clay bowl among dried herbs on pink background">BODY</div>
<div class="abs tile tile-baby" style="left:781px" role="img" aria-label="Baby care bottles, cotton swabs and a soft brush on pink background">BABY</div>

<!-- products -->
<section class="abs band"></section>
<h2 class="abs heading" style="top:1263px">PRODUCTS</h2>

<svg width="0" height="0" style="position:absolute"><defs><path id="st" d="M10 1l2.7 6 6.3.6-4.8 4.2 1.4 6.4L10 15l-5.6 3.2 1.4-6.4L1 7.6l6.3-.6z"/></defs></svg>

<article class="abs card" style="left:89px">
  <div class="shot" role="img" aria-label="Lilac lotion bottle with purple cap" style="background:radial-gradient(ellipse 14px 16px at 50% 9%,#8b60b8 0%,#8b60b8 80%,transparent 100%),radial-gradient(ellipse 50px 105px at 50% 58%,#c9a3df 0%,#b991d3 80%,transparent 100%)"></div>
  <h3>NEQUE PORRO QUISQUAM</h3>
  <div class="price">$59.95</div>
  <div class="stars"><svg width="122" height="20" viewBox="0 0 122 20" fill="#f7941d"><use href="#st"/><use href="#st" x="25"/><use href="#st" x="50"/><use href="#st" x="75"/><use href="#st" x="100"/></svg></div>
  <p>Sed ut perspiciatis unde omnis iste natus error sit voluptatem accusantium</p>
  <div class="cart">ADD TO CART</div>
</article>

<article class="abs card" style="left:437px">
  <div class="shot" role="img" aria-label="Blue and white bath product bottles with sponges and a flower" style="background:radial-gradient(ellipse 30px 90px at 52% 45%,#8fbef0 0%,#a9cdf2 70%,transparent 100%),radial-gradient(ellipse 40px 40px at 25% 68%,#4fb6e6 0%,transparent 100%),radial-gradient(ellipse 30px 60px at 78% 65%,#f1f1f1 0%,#e3e3e3 70%,transparent 100%),radial-gradient(ellipse 140px 40px at 50% 88%,#e8ecef 0%,transparent 100%)"></div>
  <div class="abs ribbon">OUT OF<br>STOCK</div>
  <h3>NEQUE PORRO QUISQUAM</h3>
  <div class="price">$ 110.00</div>
  <div class="stars"><svg width="122" height="20" viewBox="0 0 122 20" fill="#f7941d"><use href="#st"/><use href="#st" x="25"/><use href="#st" x="50"/><use href="#st" x="75"/><use href="#st" x="100"/></svg></div>
  <p>Sed ut perspiciatis unde omnis iste natus error sit voluptatem accusantium</p>
  <div class="cart on">ADD TO CART</div>
</article>

<article class="abs card" style="left:786px">
  <div class="shot" role="img" aria-label="Open jar of white cream with sliced aloe vera leaves" style="background:radial-gradient(ellipse 90px 55px at 40% 38%,#f4f4f4 0%,#e2e2e2 70%,transparent 100%),radial-gradient(ellipse 60px 45px at 72% 30%,#e9e9e9 0%,transparent 100%),radial-gradient(ellipse 110px 45px at 55% 78%,#6f9b4c 0%,#8ab567 50%,transparent 100%)"></div>
  <div class="abs" style="left:248px;top:14px;width:62px;height:62px;border-radius:50%;background:#1ee51e;display:flex;align-items:center;justify-content:center;font-family:Roboto,sans-serif;font-weight:500;font-size:20px">15%</div>
  <h3>NEQUE PORRO QUISQUAM</h3>
  <div class="price">$ 150.00</div>
  <div class="stars"><svg width="122" height="20" viewBox="0 0 122 20" fill="#f7941d"><use href="#st"/><use href="#st" x="25"/><use href="#st" x="50"/><use href="#st" x="75"/><use href="#st" x="100"/></svg></div>
  <p>Sed ut perspiciatis unde omnis iste natus error sit voluptatem accusantium</p>
  <div class="cart">ADD TO CART</div>
</article>
<div class="abs dots" style="left:576px;top:1927px"><i></i><i class="on"></i><i></i></div>

<!-- reviews -->
<h2 class="abs heading" style="top:2067px">REVIEWS</h2>
<div class="abs quote" style="left:89px;top:2230px">Lorem ipsum dolor sit amet, consectetur adipiscing elit, sed do eiusmod tempor incididunt ut labore et dolore magna aliqua. Ut enim ad minim veniam, quis nostrud exercitation ullamco laboris nisi ut aliquip ex ea commodo reprehenderit</div>
<div class="abs name" style="left:89px;top:2444px">HARLOW</div>
<div class="abs quote" style="left:448px;top:2167px">Lorem ipsum dolor sit amet, consectetur adipiscing elit, sed do eiusmod tempor incididunt ut labore et dolore magna aliqua. Ut enim ad minim veniam, quis nostrud exercitation ullamco laboris nisi ut aliquip ex ea commodo reprehenderit</div>
<div class="abs name" style="left:448px;top:2377px">BRENNER</div>
<div class="abs quote" style="left:798px;top:2230px">Lorem ipsum dolor sit amet, consectetur adipiscing elit, sed do eiusmod tempor incididunt ut labore et dolore magna aliqua. Ut enim ad minim veniam, quis nostrud exercitation ullamco laboris nisi ut aliquip ex ea commodo reprehenderit</div>
<div class="abs name" style="left:798px;top:2444px">OKAFOR</div>
<div class="abs dots" style="left:580px;top:2500px"><i></i><i class="on"></i><i></i></div>

<!-- promo -->
<section class="abs promo" role="img" aria-label="Flat lay of natural skincare: fern leaves, loofah, cream jars, bath salt scoop, soap bar, dropper bottle and a white towel"></section>
<div class="abs promo-veil"></div>
<div class="abs new">NEW</div>
<h2 class="abs promo-title">100% NATURAL ORGANIC</h2>
<div class="abs promo-sub">NATURAL SKINCARE</div>
<div class="abs promo-rule"></div>
<p class="abs promo-text">Lorem ipsum dolor sit amet, consectetur adipiscing elit, sed do eius-mod tempor incididunt ut labore et dolore magna aliqua.</p>
<div class="abs btn-fill" style="left:510px;top:2978px;width:184px;height:48px;font-size:19px;font-weight:500">SHOP NOW</div>

<!-- newsletter -->
<h2 class="abs heading" style="top:3278px">NEWSLETTER&nbsp; SIGNUP</h2>
<div class="abs field">
  <svg width="32" height="24" viewBox="0 0 32 24" fill="none" stroke="#222" stroke-width="2"><rect x="1" y="1" width="30" height="22" rx="2"/><path d="M1 2l15 12L31 2"/></svg>
  Enter your email address
</div>
<div class="abs btn-fill" style="left:784px;top:3366px;width:244px;height:71px;font-size:22px;font-weight:500">SUBSCRIBE</div>

<!-- footer -->
<footer class="abs footer"></footer>
<div class="abs" style="left:208px;top:3612px;width:60px;height:60px;border:4px solid #fff;border-radius:50%"></div>
<div class="abs" style="left:94px;top:3716px;width:287px;text-align:center;font-family:Roboto,sans-serif;font-weight:500;font-size:30px;color:#fff">QUILLOMSTORE</div>

<div class="abs f-head" style="left:439px">QUICKS LINKS</div>
<ul class="abs f-list" style="left:439px"><li>Home</li><li>Products</li><li>Review</li><li>Blog</li><li>Contact us</li></ul>
<div class="abs f-head" style="left:635px">USEFUL LINKS</div>
<ul class="abs f-list" style="left:636px"><li>Map to our store</li><li>International Shipping Info</li><li>Privacy &amp; Security</li><li>Satisfaction Guarantee</li></ul>
<div class="abs f-head" style="left:918px">CONTACT US</div>
<ul class="abs f-list" style="left:922px"><li>Quillomstore,</li><li>Lindhagsvägen 7</li><li>512 40 Vessberg</li><li>Tel: 555-20 41 77</li><li>info@quillomstore.co</li></ul>

<div class="abs" style="left:94px;top:3834px;font-size:17px;color:#fff">Copyright © 2020 quillomstore.co All Rights Reserved</div>
<div class="abs pay"><span></span><span></span><span></span><span></span><span></span><span></span></div>

</body>
</html>
```